LITTLE DESIGN WORK REQUIRED!

UPDATE: WE WEREN'T OVERLY ECSTATIC WITH THE DESIGNS WE WERE RECEIVING SO WE DID MOST OF THE DESIGN WORK OURSELVES...

PLEASE SEE THE NEWLY ATTACHED PPT DOC TO VIEW NEARLY EXACT REPLICAS OF WHAT WE WANT THE SITE TO LOOK LIKE. WE NOW NEED YOUR HELP TO MAKE IT LOOK LIKE SOMETHING WORTHY OF THE WEB.

NO CODING REQUIRED - EXPECTED OUTPUT PSD FILES

Hi everyone!

We're looking for a designer to work their magic for our site! We're a not-for-profit program aimed at helping young people realise their potential!

In the attached PPT file, you'll notice we've already DESIGNED THE ENTIRE SITE IN POWERPOINT. Now, we need YOU to make the small changes we requested in the document as well as design the whole thing in psd.

Any questions, don't hesitate to ask.

Brook-Rise
Updates

We've done about 95% of the design for you. Please fine-tune it. See the newly attached PPT doc for details. 

The best two designs will win. This project closes on Friday - please message us if you are absolutely sure you cannot make the deadline.

Thanks,
Brook-Rise

```html
<!DOCTYPE html>
<html lang="en">
<head>
<meta charset="utf-8">
<title>Brook-Rise · Resources</title>
<link rel="stylesheet" href="https://fonts.googleapis.com/css2?family=Source+Sans+3:wght@400;600;700&display=swap">
<style>
  :root {
    --grass: #7dbb1d;
    --grass-dark: #5e9a10;
    --paper: #ffffff;
    --ink: #111111;
    --ink-soft: #555555;
    --accent: #8cc21f;
    --nav-grey: #d9d9d9;
    --nav-grey-dark: #b5b5b5;
    --feature: #e23a63;
    --quick: #6fc23d;
    --footer: #000000;
    --footer-text: #e8e8e8;
    --chip: #eef3f8;
    --chip-text: #3b6ea5;
  }
  * { box-sizing: border-box; margin: 0; padding: 0; }
  html, body { width: 805px; height: 1200px; overflow: hidden; }
  body {
    position: relative;
    font-family: "Source Sans 3", sans-serif;
    color: var(--ink);
    background: linear-gradient(90deg, var(--grass-dark), var(--grass) 6%, var(--grass) 94%, var(--grass-dark));
  }
  .page {
    position: absolute; left: 98px; top: 0; width: 613px; height: 983px;
    background: var(--paper);
  }
  .brand {
    position: absolute; left: 22px; top: 30px;
    display: flex; align-items: center; gap: 8px;
    font-weight: 700; font-size: 30px; letter-spacing: 0.5px; color: #1a1a1a;
  }
  .brand-dot { width: 16px; height: 16px; border-radius: 50%; background: var(--accent); }
  .main-nav { position: absolute; top: 102px; left: 0; width: 613px; height: 24px; }
  .nav-item {
    position: absolute; top: 0; height: 24px;
    display: flex; align-items: center; justify-content: center; gap: 5px;
    font-size: 11px; color: #444;
    background: linear-gradient(#f2f2f2, var(--nav-grey));
    border: 1px solid var(--nav-grey-dark); border-radius: 2px;
  }
  .nav-item::after { content: ""; width: 0; height: 0; border-left: 3px solid transparent; border-right: 3px solid transparent; border-top: 3px solid #888; }
  .nav-item.is-active { background: linear-gradient(#9bd12f, #62a40f); border-color: #5a9610; color: #fff; }
  .nav-item.is-active::after { border-top-color: #fff; }
  .section-title { position: absolute; left: 16px; top: 145px; font-size: 18px; font-weight: 400; color: var(--accent); }
  .intro {
    position: absolute; left: 16px; top: 176px; width: 580px;
    font-size: 11.4px; line-height: 15px; text-transform: uppercase; color: #222;
  }
  .card { position: absolute; width: 178px; }
  .card-tag { font-size: 11px; color: #222; height: 14px; display: flex; align-items: center; gap: 4px; }
  .card-tag::after { content: ""; border-left: 3px solid transparent; border-right: 3px solid transparent; border-top: 3px solid #222; }
  .card-media { position: relative; margin-top: -2px; height: 116px; transform: translateY(12px); }
  .badge {
    position: absolute; right: 0; bottom: 8px; width: 82px; height: 18px;
    display: flex; align-items: center; justify-content: center;
    font-size: 13px; color: #fff; letter-spacing: 0.3px;
  }
  .badge.feature { background: var(--feature); }
  .badge.quick { background: var(--quick); width: 98px; }
  .play { position: absolute; left: 72px; top: 40px; }
  .card-title { position: absolute; left: 0; top: 146px; font-size: 10.5px; font-weight: 700; line-height: 12px; width: 178px; }
  .card-text { position: absolute; left: 0; font-size: 8.6px; line-height: 11px; color: var(--ink-soft); width: 178px; }
  .share { position: absolute; top: 190px; display: flex; gap: 3px; align-items: center; }
  .chip { height: 11px; padding: 0 4px; font-size: 7px; display: flex; align-items: center; gap: 2px; background: var(--chip); color: var(--chip-text); border: 1px solid #c8d6e6; border-radius: 2px; }
  .chip::before { content: ""; width: 5px; height: 5px; background: #7aa4cf; border-radius: 1px; }
  .count { width: 20px; height: 12px; background: #111; color: #fff; font-size: 7.5px; display: flex; align-items: center; justify-content: center; }
  .site-footer { position: absolute; left: 0; top: 983px; width: 805px; height: 217px; background: var(--footer); color: var(--footer-text); }
  .footer-col { position: absolute; top: 22px; width: 160px; text-align: center; }
  .footer-col h2 { font-size: 13px; font-weight: 400; padding-bottom: 7px; border-bottom: 1px solid #333; margin-bottom: 10px; }
  .footer-links li { list-style: none; font-size: 9.5px; line-height: 18px; }
  .footer-contact p { font-size: 9.5px; line-height: 19px; }
  .social { display: flex; justify-content: center; gap: 6px; }
  .social span { width: 30px; height: 30px; border-radius: 5px; background: linear-gradient(#8fa6bf, #4d6580); }
</style>
</head>
<body>
  <main class="page">
    <div class="brand"><span>BROOK-RISE</span><span class="brand-dot"></span></div>

    <nav class="main-nav">
      <div class="nav-item" style="left:31px;width:68px">Home</div>
      <div class="nav-item" style="left:125px;width:75px">About Us</div>
      <div class="nav-item is-active" style="left:219px;width:75px">Resources</div>
      <div class="nav-item" style="left:314px;width:81px">Workshops</div>
      <div class="nav-item" style="left:415px;width:86px">Ambassadors</div>
      <div class="nav-item" style="left:523px;width:56px">Feats</div>
    </nav>

    <h1 class="section-title">RESOURCES</h1>
    <p class="intro">Brook-Rise provides a number of resources, from success stories and motivational videos , to interviews with our Brook-Rise ambassadors. We're confident each post will get you that much closer to reaching your authentic, meaningful, and audacious goals.</p>

    <!-- Row 1 -->
    <article class="card" style="left:16px;top:240px">
      <div class="card-tag">Design</div>
      <div class="card-media" role="img" aria-label="Photo of a group of volunteers standing against the sky" style="background:linear-gradient(#c4d0df,#8e9399 60%,#5a5450)"><div class="badge feature">FEATURE</div></div>
      <h3 class="card-title">How to join the Service Corps</h3>
      <p class="card-text" style="top:167px">Thinking of joining the Service Corps? Think haerder.</p>
      <div class="share" style="left:80px"><span class="chip">Share</span><span class="chip">Like</span><span class="count">3</span></div>
    </article>
    <article class="card" style="left:215px;top:240px">
      <div class="card-tag">Build</div>
      <div class="card-media" role="img" aria-label="Photo of a smiling girl in a swimsuit" style="background:linear-gradient(135deg,#b58f73,#d8b49a 50%,#9c7b66)"><div class="badge quick">QUICK-READ</div></div>
      <h3 class="card-title">How to bucket shower like a pro</h3>
      <p class="card-text" style="top:167px">The scenario: You have only one bucket of water.</p>
      <div class="share" style="left:80px"><span class="chip">Share</span><span class="chip">Like</span><span class="count">3</span></div>
    </article>
    <article class="card" style="left:415px;top:240px">
      <div class="card-tag">Achieve</div>
      <div class="card-media" role="img" aria-label="Photo of a monastery courtyard with arched galleries" style="background:linear-gradient(#b7a6c0,#7d5f86 55%,#4a3a52)"><div class="badge feature">FEATURE</div></div>
      <h3 class="card-title">How to sleep in a Bulgarian monk's cell</h3>
      <p class="card-text" style="top:167px">Hitchhike to the sou thwestern Rila Mountains in Bulgaria.</p>
      <div class="share" style="left:80px"><span class="chip">Share</span><span class="chip">Like</span><span class="count">3</span></div>
    </article>

    <!-- Row 2 -->
    <article class="card" style="left:16px;top:471px">
      <div class="card-tag">Design</div>
      <div class="card-media" role="img" aria-label="Video still of a skier on a snowy mountain slope" style="background:linear-gradient(#5a6e95,#a9b6cc 45%,#eef1f5)">
        <svg class="play" width="34" height="34" viewBox="0 0 34 34"><rect width="34" height="34" rx="5" fill="#000" opacity=".45"/><path d="M12 8 L26 17 L12 26 Z" fill="#fff" opacity=".8"/></svg>
      </div>
      <h3 class="card-title">9 days on BC's Powder Highway in 3 minutes</h3>
      <p class="card-text" style="top:180px">Colorado was hurthing for snow ; it was practically still summer in Tahoe and Mammoth.</p>
      <div class="share" style="left:80px;top:211px"><span class="chip">Share</span><span class="chip">Like</span><span class="count">3</span></div>
    </article>
    <article class="card" style="left:215px;top:471px">
      <div class="card-tag">Discover</div>
      <div class="card-media" role="img" aria-label="Illustration of an open book with a character on a yellow background" style="background:linear-gradient(#f4d21f,#eec313)"><div class="badge quick">QUICK-READ</div></div>
      <h3 class="card-title">Language learning hack: Translate the web</h3>
      <p class="card-text" style="top:180px">The ultimate goal of Lingofy is to translate the web, one page at a time.</p>
      <div class="share" style="left:80px;top:211px"><span class="chip">Share</span><span class="chip">Like</span><span class="count">3</span></div>
    </article>
    <article class="card" style="left:415px;top:471px">
      <div class="card-tag">Design</div>
      <div class="card-media" role="img" aria-label="Video still of the sun's fiery surface" style="background:radial-gradient(circle at 40% 40%,#f0641c,#b51d0a 55%,#3a0805)">
        <svg class="play" width="34" height="34" viewBox="0 0 34 34"><rect width="34" height="34" rx="5" fill="#000" opacity=".45"/><path d="M12 8 L26 17 L12 26 Z" fill="#fff" opacity=".8"/></svg>
      </div>
      <h3 class="card-title">7 stunning videos of our solar system</h3>
      <p class="card-text" style="top:167px">Groundbreaking footage of space travel from 1946 to the present.</p>
      <div class="share" style="left:80px;top:211px"><span class="chip">Share</span><span class="chip">Like</span><span class="count">3</span></div>
    </article>

    <!-- Row 3 -->
    <article class="card" style="left:16px;top:720px">
      <div class="card-tag">Discover</div>
      <div class="card-media" role="img" aria-label="Photo of a group of volunteers standing against the sky" style="background:linear-gradient(#c4d0df,#8e9399 60%,#5a5450)"><div class="badge feature">FEATURE</div></div>
      <h3 class="card-title">How to join Crops</h3>
      <p class="card-text" style="top:167px">Thinking of joining the Servise Corps? Think harder.</p>
      <div class="share" style="left:80px;top:196px"><span class="chip">Share</span><span class="chip">Like</span><span class="count">3</span></div>
    </article>
    <article class="card" style="left:215px;top:720px">
      <div class="card-tag">Design</div>
      <div class="card-media" role="img" aria-label="Photo of a smiling girl in a swimsuit" style="background:linear-gradient(135deg,#b58f73,#d8b49a 50%,#9c7b66)"><div class="badge quick">QUICK-READ</div></div>
      <h3 class="card-title">How to bucket shower like a pro</h3>
      <p class="card-text" style="top:167px">The scenario : You habe only one bucket of water.</p>
      <div class="share" style="left:80px;top:196px"><span class="chip">Share</span><span class="chip">Like</span><span class="count">3</span></div>
    </article>
    <article class="card" style="left:415px;top:720px">
      <div class="card-tag">Build</div>
      <div class="card-media" role="img" aria-label="Photo of a monastery courtyard with arched galleries" style="background:linear-gradient(#b7a6c0,#7d5f86 55%,#4a3a52)"><div class="badge feature">FEATURE</div></div>
      <h3 class="card-title">How to sleep in a bulgraina monk's cell</h3>
      <p class="card-text" style="top:167px">Hitchhike to the southwestern rila Mountains in Bulgaria.</p>
      <div class="share" style="left:80px;top:196px"><span class="chip">Share</span><span class="chip">Like</span><span class="count">3</span></div>
    </article>
  </main>

  <footer class="site-footer">
    <section class="footer-col" style="left:76px">
      <h2>Site Navigation</h2>
      <ul class="footer-links">
        <li>Home</li><li>About Us</li><li>Resources</li><li>Workshops</li><li>Ambassadors</li><li>Feats</li>
      </ul>
    </section>
    <section class="footer-col" style="left:325px">
      <h2>Follow Us</h2>
      <div class="social"><span></span><span></span><span></span><span></span></div>
    </section>
    <section class="footer-col footer-contact" style="left:559px">
      <h2>Contact Us</h2>
      <p>48 Harbor Road, Suite no.14</p>
      <p>street no.310 near Mira Bakery</p>
      <p>Postal code: 402-kmn</p>
    </section>
  </footer>
</body>
</html>
```